Brightford Lingua Partners, LLC

We need a business card that includes information about our business and conveys a reliable business that provides document translation services and interpreters for a variety of corporate and individual clients. We want to come across as professional, reliable, yet approachable. It should include the following on one side:

ESL / ENL Language Classes, Private Lessons, and Online Tutors
PALQE Training and Testing
Translating & Interpreting Services
Contact us about Over-the-Phone Interpreting in over 200 languages
24/7/365
www.brightfordlingua.example

The other side should include (555) 481-3062

Marla Quennick, President
412 Garvin Ave., Ste. 209
Indianapolis, IN 46999
Updates

Please add USA as part of the address. Also, please add mrqquennick@brightfordlinguapartners.example as the e-mail address. Thank you.

Target Market(s)

Business professionals, their families, the international community

Industry/Entity Type

Business

Contact Information for Business Card

24/7/365
www.brightfordlingua.example

(555) 481-3062

Marla Quennick, President
412 Garvin Ave., Ste. 209
Indianapolis, IN 46999
USA

Font styles to use
Sans Serif

Colors

Designer to choose colors to be used in the design.

Requirements
Must have
• See project description
• e-mail address and web address
• Phone number
Nice to have
• a globe
• physical address
Should not have
• Should not have the same color scheme as other agencies in our market in Indiana unless it is blue and black. No purple or yellow.

```html
<!DOCTYPE html>
<html lang="en">
<head>
<meta charset="utf-8">
<title>Brightford Lingua Partners – Business Card</title>
<link rel="stylesheet" href="https://fonts.googleapis.com/css2?family=Montserrat:wght@500;700&family=Roboto+Condensed:wght@700&display=swap">
<style>
  :root {
    --brand-blue: #2390d2;
    --edge-blue: #a9cdf0;
    --ink: #111111;
    --paper: #ffffff;
    --backdrop: #e7e9ec;
  }
  * { box-sizing: border-box; margin: 0; padding: 0; }
  html, body { width: 1200px; height: 1200px; overflow: hidden; }
  body {
    background: var(--backdrop);
    font-family: "Montserrat", sans-serif;
    color: var(--ink);
    display: flex;
    flex-direction: column;
    align-items: center;
    justify-content: center;
    gap: 40px;
  }
  .card {
    position: relative;
    width: 910px;
    height: 520px;
    background: var(--paper);
    overflow: hidden;
    box-shadow: 0 6px 18px rgba(0,0,0,0.18);
  }
  .card__art { position: absolute; inset: 0; width: 100%; height: 100%; }
  .brand {
    position: absolute;
    top: 48px;
    left: 48px;
    display: flex;
    align-items: center;
    gap: 22px;
  }
  .brand__dot {
    width: 120px;
    height: 120px;
    border-radius: 50%;
    background: var(--brand-blue);
    flex: none;
  }
  .brand__name {
    font-family: "Montserrat", sans-serif;
    font-weight: 500;
    font-size: 40px;
    line-height: 1.02;
    color: var(--ink);
  }
  .brand__name span { display: block; }

  /* Services side */
  .services {
    position: absolute;
    right: 44px;
    top: 238px;
    text-align: right;
    font-family: "Roboto Condensed", sans-serif;
    font-weight: 700;
    font-size: 19px;
    line-height: 1.32;
  }
  .contact-list {
    position: absolute;
    right: 44px;
    bottom: 34px;
    list-style: none;
    text-align: right;
    font-family: "Roboto Condensed", sans-serif;
    font-weight: 700;
    font-size: 18px;
    line-height: 1.5;
  }
  .contact-list li { display: flex; justify-content: flex-end; align-items: center; gap: 10px; }
  .contact-list svg { width: 20px; height: 20px; flex: none; }
  .contact-list .contact-list__web { font-family: "Montserrat", sans-serif; font-weight: 500; font-size: 20px; }

  /* Contact side */
  .details {
    position: absolute;
    right: 46px;
    top: 70px;
    text-align: right;
    font-weight: 700;
    font-size: 27px;
    line-height: 1.32;
  }
  .details__phone { font-size: 33px; margin-bottom: 4px; }
</style>
</head>
<body>

  <section class="card card--services" aria-label="Card front: services">
    <svg class="card__art" viewBox="0 0 910 520" preserveAspectRatio="none" aria-hidden="true">
      <path d="M300 520 C 390 330, 600 215, 910 190 L910 520 Z" fill="var(--edge-blue)"/>
      <path d="M322 520 C 410 342, 612 230, 910 206 L910 520 Z" fill="var(--brand-blue)"/>
    </svg>
    <div class="brand">
      <div class="brand__dot"></div>
      <p class="brand__name"><span>Brightford</span><span>Lingua</span><span>Partners, LLC</span></p>
    </div>
    <div class="services">
      <p>ESL / ENL Language Classes, Private Lessons, and Online Tutors</p>
      <p>PALQE Training and Testing</p>
      <p>Translating &amp; Interpreting Services</p>
      <p>Contact us about Over-the-Phone Interpreting in over 200 languages</p>
      <p>24/7/365</p>
    </div>
    <ul class="contact-list">
      <li>(555) 481-3062
        <svg viewBox="0 0 24 24" aria-hidden="true"><path d="M6.6 10.8a15.1 15.1 0 0 0 6.6 6.6l2.2-2.2a1 1 0 0 1 1-.25 11.4 11.4 0 0 0 3.6.57 1 1 0 0 1 1 1V20a1 1 0 0 1-1 1A17 17 0 0 1 3 4a1 1 0 0 1 1-1h3.5a1 1 0 0 1 1 1c0 1.25.2 2.45.57 3.57a1 1 0 0 1-.25 1z" fill="none" stroke="var(--ink)" stroke-width="1.6"/></svg>
      </li>
      <li>mrqquennick@brightfordlinguapartners.example
        <svg viewBox="0 0 24 24" aria-hidden="true"><rect x="3" y="5" width="18" height="14" fill="none" stroke="var(--ink)" stroke-width="1.6"/><path d="M3 5l9 8 9-8" fill="none" stroke="var(--ink)" stroke-width="1.6"/></svg>
      </li>
      <li class="contact-list__web">www.brightfordlingua.example
        <svg viewBox="0 0 24 24" aria-hidden="true"><circle cx="12" cy="12" r="9" fill="none" stroke="var(--ink)" stroke-width="1.6"/><ellipse cx="12" cy="12" rx="4" ry="9" fill="none" stroke="var(--ink)" stroke-width="1.4"/><path d="M3 12h18M5 7h14M5 17h14" stroke="var(--ink)" stroke-width="1.2"/></svg>
      </li>
    </ul>
  </section>

  <section class="card card--contact" aria-label="Card back: contact details">
    <svg class="card__art" viewBox="0 0 910 520" preserveAspectRatio="none" aria-hidden="true">
      <rect x="0" y="350" width="910" height="170" fill="var(--edge-blue)"/>
      <rect x="0" y="362" width="910" height="158" fill="var(--brand-blue)"/>
    </svg>
    <div class="brand">
      <div class="brand__dot"></div>
      <p class="brand__name"><span>Brightford</span><span>Lingua</span><span>Partners, LLC</span></p>
    </div>
    <address class="details" style="font-style:normal">
      <p class="details__phone">(555) 481-3062</p>
      <p>Marla Quennick, President</p>
      <p>412 Garvin Ave., Ste. 209</p>
      <p>Indianapolis, IN 46999</p>
      <p>USA</p>
    </address>
  </section>

</body>
</html>
```